Stationery design for a hip Muslim Travel Agency

We are looking for a colorful and energetic stationery design for a Muslim tour and travel agency. We need a letterhead, A4 folder, business card and loyalty card design.

The designs should be clean and cheerful and have a feeling of a colorful mosaic in a mosque. You can use the Facebook avatar and cover photo as the basis.

Rimbelu card is a loyalty card we issue to our clients. This can have a similar feel to the business card and it should NOT have the word "card" added to the logo. Think of airline membership cards.

Target Market(s)

Indonesians, 25-44 years old, Muslim, interesting in Umroh and Haji and other Muslim tours.

Industry/Entity Type

Travel Agent

Contact Information for Business Card

As provided in the .psd file.

Font styles to use
Sans Serif

Colors
27a0d5
33b8a4
00a990
0492cd

Requirements
Must have
• Letterhead design
• A4 folder design
• Business card
• Loyalty card (without the word "card" in the logo)
Nice to have
• Use the mosaic patterns provided in the files. We want to express the theme of colorful Islam.
Should not have
• Don't copy the .psd files provided in the brief. This is just for the content, those files were not prepared by a designer.

```html
<!DOCTYPE html>
<html lang="id">
<head>
<meta charset="utf-8">
<title>Rimbelu Letterhead</title>
<link href="https://fonts.googleapis.com/css2?family=Montserrat:wght@400;700&display=swap" rel="stylesheet">
<style>
  :root {
    --teal: #33b8a4;
    --lime: #a8cf38;
    --ink: #2b2b2b;
    --paper: #ffffff;
    --backdrop: #9b9b9b;
  }
  html, body {
    margin: 0;
    width: 926px;
    height: 1200px;
    overflow: hidden;
    background: var(--backdrop);
  }
  .letterhead {
    position: absolute;
    left: 39px;
    top: 0;
    width: 957px;
    height: 1355px;
    background: var(--paper);
    transform: scale(0.8856);
    transform-origin: 0 0;
    font-family: "Montserrat", sans-serif;
    color: var(--ink);
  }
  .bands {
    position: absolute;
    inset: 0;
    width: 957px;
    height: 1355px;
  }
  .brand {
    position: absolute;
    left: 53px;
    top: 112px;
    display: flex;
    align-items: center;
    gap: 14px;
  }
  .brand-dot {
    width: 50px;
    height: 50px;
    border-radius: 50%;
    background: var(--teal);
  }
  .brand-name {
    font-weight: 700;
    font-size: 38px;
    letter-spacing: 1px;
    color: var(--ink);
  }
  .address {
    position: absolute;
    right: 45px;
    top: 119px;
    text-align: right;
    font-size: 16px;
    line-height: 26px;
    color: #222;
  }
  .address .phone {
    display: inline-flex;
    align-items: center;
    gap: 10px;
  }
  .footer-contacts {
    position: absolute;
    left: 0;
    top: 1299px;
    height: 56px;
    display: flex;
    align-items: center;
    font-size: 15px;
    color: #fff;
  }
  .contact {
    position: absolute;
    display: flex;
    align-items: center;
    gap: 10px;
    white-space: nowrap;
  }
  .contact .mark {
    width: 9px;
    height: 9px;
    background: #fff;
    border-radius: 2px;
  }
</style>
</head>
<body>
  <main class="letterhead">
    <svg class="bands" viewBox="0 0 957 1355" aria-hidden="true">
      <polygon fill="var(--teal)" points="0,0 957,0 957,55 270,55 220,90 0,90"/>
      <polygon fill="var(--lime)" points="0,52 205,52 255,17 957,17 957,35 262,35 212,72 0,72"/>
      <polygon fill="var(--teal)" points="0,1299 763,1299 713,1355 0,1355"/>
      <polygon fill="var(--lime)" points="780,1299 957,1299 957,1355 727,1355"/>
    </svg>

    <header>
      <div class="brand">
        <span class="brand-dot"></span>
        <span class="brand-name">rimbelu.id</span>
      </div>
      <address class="address" style="font-style:normal">
        Jl. Melati Raya No. 14 Gandaria Utara<br>
        Kebayoran Baru, Jakarta Selatan 12140<br>
        <span class="phone">
          <svg width="14" height="16" viewBox="0 0 24 24" aria-hidden="true"><path fill="#222" d="M6.6 10.8a15.1 15.1 0 0 0 6.6 6.6l2.2-2.2c.3-.3.7-.4 1-.2 1.1.4 2.3.6 3.6.6.6 0 1 .4 1 1V20c0 .6-.4 1-1 1C10.6 21 3 13.4 3 4c0-.6.4-1 1-1h3.5c.6 0 1 .4 1 1 0 1.3.2 2.5.6 3.6.1.3 0 .7-.2 1L6.6 10.8z"/></svg>
          0888-RIMBELU (7462358)
        </span>
      </address>
    </header>

    <footer class="footer-contacts">
      <span class="contact" style="left:50px">
        <svg width="11" height="8" viewBox="0 0 11 8" aria-hidden="true"><rect width="11" height="8" fill="#fff"/><path d="M0 0 L5.5 4.5 L11 0" stroke="var(--teal)" fill="none"/></svg>
        salam@rimbelu.id
      </span>
      <span class="contact" style="left:274px"><span class="mark"></span>rimbelu.id</span>
      <span class="contact" style="left:426px"><span class="mark"></span>Rimbelu</span>
      <span class="contact" style="left:562px"><span class="mark"></span>Rimbelu Indonesia</span>
    </footer>
  </main>
</body>
</html>
```